Tunnel

a graphic meme to be sent to my clients, consisting of a long angular dark tunnel with a bright light at one end; located within the bright light at the end of the tunnel is the number 2021
the illuminated (shiny silver?) 3 dimensional font message running along the left wall of the tunnel is: BE SAFE.!
the smaller font message underneath the graphic is: Best Wishes For a Healthy New Year
Dan Marlowe Mediator (also to be included nearby is a small semi-circle logo of my corporate logo).

Font styles to use
Sans Serif
Other font styles liked:
• 3 dimensional bold lettering for BE SAFE

```html
<!DOCTYPE html>
<html lang="en">
<head>
<meta charset="utf-8">
<title>2021 Be Safe – New Year Greeting</title>
<link rel="stylesheet" href="https://fonts.googleapis.com/css2?family=Montserrat:wght@700&family=Nunito:wght@900&family=Oswald:wght@500;700&family=Yanone+Kaffeesatz:wght@400&display=swap">
<style>
  :root {
    --frame-dark: #1c0709;
    --band-maroon: #3b0c10;
    --light-core: #fffdf4;
    --light-warm: #e9c99a;
    --wall-tan: #9a7a5a;
    --wall-shadow: #2a2c30;
    --wall-steel: #4f6670;
    --year-orange: #e0a060;
    --safe-white: #ffffff;
    --safe-shadow: #0d2038;
    --wish-cream: #f4e9a6;
    --name-white: #ffffff;
    --badge-navy: #1d2466;
  }
  html, body {
    margin: 0;
    padding: 0;
    width: 1200px;
    height: 846px;
    overflow: hidden;
    background: var(--band-maroon);
  }
  .greeting-card {
    position: relative;
    width: 1200px;
    height: 846px;
    background: var(--band-maroon);
    overflow: hidden;
  }
  .top-edge {
    position: absolute;
    left: 0; top: 0;
    width: 1200px; height: 20px;
    background: var(--frame-dark);
  }
  .tunnel-scene {
    position: absolute;
    left: 0; top: 20px;
    width: 1200px; height: 645px;
    background:
      radial-gradient(ellipse 170px 150px at 360px 440px, var(--light-core) 0%, rgba(255,253,244,0.85) 45%, rgba(255,253,244,0) 100%),
      radial-gradient(ellipse 520px 420px at 340px 420px, rgba(233,201,154,0.9) 0%, rgba(154,122,90,0.55) 55%, rgba(154,122,90,0) 100%),
      linear-gradient(100deg, var(--wall-tan) 0%, #6b5b4b 35%, var(--wall-shadow) 60%, var(--wall-steel) 100%);
  }
  .headline {
    position: absolute;
    left: 0; top: 0;
    width: 1200px; height: 665px;
  }
  .year {
    font-family: "Nunito", sans-serif;
    font-weight: 900;
    fill: var(--year-orange);
  }
  .be-safe {
    font-family: "Oswald", sans-serif;
    font-weight: 700;
    fill: var(--safe-white);
    filter: drop-shadow(4px 5px 3px var(--safe-shadow));
  }
  .message-band {
    position: absolute;
    left: 0; top: 665px;
    width: 1200px; height: 181px;
    background: var(--band-maroon);
  }
  .wishes {
    position: absolute;
    left: 108px; top: 664px;
    margin: 0;
    font-family: "Yanone Kaffeesatz", sans-serif;
    font-weight: 400;
    font-size: 65px;
    line-height: 80px;
    letter-spacing: 1px;
    color: var(--wish-cream);
    white-space: nowrap;
  }
  .wishes-rule {
    position: absolute;
    left: 107px; top: 748px;
    width: 765px; height: 2px;
    background: var(--wish-cream);
  }
  .signature {
    position: absolute;
    left: 212px; top: 756px;
    margin: 0;
    white-space: nowrap;
    color: var(--name-white);
    font-family: "Montserrat", sans-serif;
    font-weight: 700;
    line-height: 56px;
  }
  .signature .name { font-size: 40px; letter-spacing: 2px; }
  .signature .role { font-size: 29px; margin-left: 34px; letter-spacing: 0.5px; }
  .firm-mark {
    position: absolute;
    left: 950px; top: 700px;
    width: 200px;
    display: flex;
    flex-direction: column;
    align-items: center;
    gap: 8px;
  }
  .firm-mark .badge {
    width: 56px; height: 56px;
    border-radius: 50%;
    background: var(--badge-navy);
  }
  .firm-mark .firm-name {
    font-family: "Oswald", sans-serif;
    font-weight: 500;
    font-size: 26px;
    color: var(--wish-cream);
    letter-spacing: 1px;
  }
</style>
</head>
<body>
<main class="greeting-card">
  <div class="top-edge"></div>
  <div class="tunnel-scene" role="img" aria-label="Photo of a long arched stone tunnel with a road leading to a bright glowing light at its far end"></div>

  <svg class="headline" viewBox="0 0 1200 665" width="1200" height="665" aria-label="2021 Be Safe!">
    <text class="year" x="190" y="523" font-size="112" textLength="325" lengthAdjust="spacingAndGlyphs">2021</text>
    <g class="be-safe">
      <text x="592" y="512" font-size="83" textLength="33" lengthAdjust="spacingAndGlyphs">B</text>
      <text x="630" y="515" font-size="86" textLength="30" lengthAdjust="spacingAndGlyphs">E</text>
      <text x="682" y="525" font-size="112" textLength="43" lengthAdjust="spacingAndGlyphs">S</text>
      <text x="729" y="535" font-size="135" textLength="61" lengthAdjust="spacingAndGlyphs">A</text>
      <text x="802" y="545" font-size="160" textLength="66" lengthAdjust="spacingAndGlyphs">F</text>
      <text x="882" y="560" font-size="192" textLength="92" lengthAdjust="spacingAndGlyphs">E</text>
      <text x="996" y="570" font-size="212" textLength="56" lengthAdjust="spacingAndGlyphs">!</text>
    </g>
  </svg>

  <section class="message-band"></section>
  <p class="wishes">Best Wishes For a Healthy New Year!</p>
  <div class="wishes-rule"></div>
  <p class="signature"><span class="name">Dan Marlowe</span><span class="role">Mediator</span></p>

  <div class="firm-mark">
    <span class="badge"></span>
    <span class="firm-name">Harlan Reese</span>
  </div>
</main>
</body>
</html>
```